Your Ridgeview Homefinder Website Design

Creative Brief: Website Design for Your Ridgeview Homefinder
- Project Overview: Design a website for our new brand, "Your Ridgeview Homefinder". Your Ridgeview Homefinder is a service that matches clients with the perfect realtor. The primary function of this site is to serve as a lead generation hub, to generate leads of people who are looking to either buy or sell their house and need a great realtor. The site needs to have a very clean, modern design using sites like Quillmark, Lumhaven, Trevista, and Pravlo as an example. The site also needs to have a primary lead capture capability through a multi-step form or questionnaire that indicates if they are buying or selling, and depending on that selection, creates two different flows.

Target Audience:
- Homebuyers and sellers in the Denver area
- Individuals looking for high-quality realtor services
- Users seeking a seamless and professional online & home buying/selling experience

Objectives:
- Create a visually appealing, modern website with a strong emphasis on lead generation.
- Design advanced, multi-step forms for efficient lead capture.
- Ensure the website is user-friendly and optimized for both desktop and mobile devices.

Pages to Design:
Home Page:
- Engaging hero section with a clear call to action and the ability to enter the form flow
- Brief introduction to Your Ridgeview Homefinder and its unique value proposition
- Key features & benefits of being matched with a realtor by Your Ridgeview Homefinder
- Testimonials and success stories
- Lead capture form

About Page:
- Overview of Your Ridgeview Homefinder’s mission and values
- Professional and trust-building imagery

How it Works Page:
- Step-by-step explanation of the matching process (complete the form and we will match you with a realtor)
- Visual aids (icons, graphics) to simplify complex information
- Customer journey map from inquiry to successful match & sale of home
- Lead capture form

Contact Us Page:
- Simple and accessible contact form
- Contact details
- Call to action for immediate inquiries

Blog Template:
- Clean, easy-to-read layout for blog posts, primarily location/neighborhood guides as well as standard blogs
- Sidebar for recent posts, categories, and tags
- Social sharing buttons
- Lead capture form embedded within blog posts

Design Style:
- Modern and professional with a focus on usability
- Clean lines and intuitive navigation
- Use of curved corners and minimal straight lines for a sleek look
- Incorporation of graphic design elements, potentially including 3D and isomorphic design
- Inspired by sites like Quillmark, Lumhaven, Trevista, and Pravlo
Consistent color scheme and typography

Visual References:
- Quillmark: For its professional and corporate look
- Lumhaven and Trevista: For their user-friendly interfaces and modern design
- Pravlo: For its clean and functional layout

Target Market(s)

- Homebuyers and sellers in the Denver area, Individuals looking for high-quality realtor services, Users seeking a seamless and professional home buying/selling experience

Industry/Entity Type

Real Estate

Number of Pages Required

5+ page

Requirements
Must have
• Fully designed website with lead capture functionality based on brief
Nice to have
• Designed in Figma, Starting / Placeholder copy

```html
<!DOCTYPE html>
<html lang="en">
<head>
<meta charset="utf-8">
<title>Your Ridgeview Homefinder</title>
<link href="https://fonts.googleapis.com/css2?family=Outfit:wght@300;400;500;600&family=Lora:wght@600&display=swap" rel="stylesheet">
<style>
:root{
  --coral:#F0644E;
  --coral-soft:#F6A295;
  --cream:#FDF3E3;
  --sand:#F5CF8F;
  --blush:#FEF5F1;
  --ink:#1E1A17;
  --muted:#5E5752;
  --line:#D9CFC2;
  --footer:#2C1A0A;
  --white:#ffffff;
}
*{box-sizing:border-box;margin:0;padding:0}
html,body{width:1200px;height:5268px;overflow:hidden}
body{font-family:'Outfit',sans-serif;color:var(--ink);background:var(--cream);position:relative}
.brand{font-family:'Lora',serif;font-weight:600;color:var(--coral);font-size:18px}
a{color:inherit;text-decoration:none}

/* nav */
.site-nav{position:absolute;top:0;left:0;width:1200px;height:60px;background:var(--white);display:flex;align-items:center;justify-content:space-between;padding:0 52px}
.site-nav ul{display:flex;list-style:none;gap:30px;align-items:center;font-size:13px}
.btn{display:inline-flex;align-items:center;justify-content:center;background:var(--coral);color:var(--white);border-radius:30px;font-size:13px;font-weight:500}
.site-nav .btn{height:34px;padding:0 18px}

/* hero */
.hero{position:absolute;top:60px;left:0;width:1200px;height:680px}
.hero-photo{position:absolute;inset:0;background:linear-gradient(180deg,#4a5a3e 0%,#5b4a37 45%,#3d3a2c 75%,#6c7868 100%)}
.hero h1{position:absolute;top:225px;width:100%;text-align:center;color:var(--white);font-weight:500;font-size:46px;line-height:62px;letter-spacing:-.5px}
.search{position:absolute;left:212px;top:392px;width:660px}
.search-tabs{display:flex;background:var(--white);width:92px;border-radius:8px 8px 0 0;padding:6px 6px 0;font-size:11px}
.search-tabs span{padding:4px 10px;border-radius:6px}
.search-tabs .on{background:#E6E6E6}
.search-bar{background:var(--white);border-radius:0 10px 10px 10px;height:64px;display:flex;align-items:center;padding:0 14px}
.field{flex:1;padding:0 12px;font-size:11px}
.field+.field{border-left:1px solid var(--line)}
.field b{display:block;font-weight:500;margin-bottom:6px}
.field i{color:#8a8480;font-size:10px}
.search .btn{height:30px;padding:0 22px;font-size:11px}

/* intro */
.intro{position:absolute;top:740px;left:0;width:1200px;height:932px;text-align:center}
.intro h2{margin-top:94px;font-size:38px;font-weight:500;line-height:48px}
.intro p{width:560px;margin:30px auto 0;font-size:13px;line-height:23px;color:var(--muted)}
.rule{width:648px;margin:32px auto 0;border-top:1px solid var(--line)}
.featured{margin-top:22px;font-size:10px;letter-spacing:1.5px;color:var(--muted)}
.press{display:flex;justify-content:center;gap:66px;margin-top:26px;font-size:24px;font-weight:600;color:#9C958F}
.intro-art{position:absolute;left:388px;bottom:0;width:748px;height:405px;border-radius:300px 300px 0 0;background:linear-gradient(180deg,#F9CFC5 0%,#F3A699 60%,#EF7E6C 100%)}

/* why */
.why{position:absolute;top:1672px;left:0;width:1200px;height:795px;background:var(--sand)}
.why-photo{position:absolute;left:51px;top:139px;width:558px;height:513px;border-radius:16px;background:linear-gradient(135deg,#d9c6a8,#9eb1c4 60%,#6a7f95)}
.agent-card{position:absolute;left:98px;top:96px;width:276px;height:98px;background:rgba(255,255,255,.55);border-radius:14px;display:flex;align-items:center;gap:14px;padding:0 28px;font-size:12px}
.avatar{width:42px;height:42px;border-radius:50%;background:#B9A58E;flex:none}
.stars{color:#F2B632;letter-spacing:3px;font-size:15px;margin-top:4px}
.sold-card{position:absolute;left:378px;top:592px;width:298px;height:110px;background:rgba(253,243,227,.92);border-radius:14px;display:flex;align-items:center;gap:18px;padding:0 34px;font-size:12px}
.sold-card .dot{width:72px;height:72px;border-radius:50%;background:#F3D9D2;flex:none}
.sold-card strong{display:block;font-size:30px;font-weight:500}
.why h2{position:absolute;left:712px;top:156px;font-size:38px;font-weight:500}
.features{position:absolute;left:712px;top:232px;width:438px;list-style:none}
.features li{display:flex;gap:22px;margin-bottom:42px}
.icon{width:44px;height:44px;border-radius:12px;background:var(--cream);flex:none;display:flex;align-items:center;justify-content:center}
.features h3{font-size:18px;font-weight:500;margin-bottom:12px}
.features p{font-size:11px;line-height:20px;color:var(--muted)}

/* stories */
.stories{position:absolute;top:2467px;left:0;width:1200px;height:670px;overflow:hidden}
.stories h2{position:absolute;left:49px;top:102px;font-size:38px;font-weight:500}
.stories .lead{position:absolute;left:49px;top:165px;font-size:13px;color:var(--muted)}
.quotes{position:absolute;left:49px;top:252px;display:flex;gap:28px}
.quote{width:348px;height:255px;border:1.5px solid #DAC3A4;border-radius:14px;padding:28px 26px;font-size:13px;line-height:22.5px;display:flex;flex-direction:column;justify-content:space-between}
.who{display:flex;gap:16px;align-items:center;font-size:11px;line-height:17px}
.who .avatar{width:42px;height:42px}
.who span{color:var(--muted)}
.pager{position:absolute;left:49px;top:552px;display:flex;gap:7px}
.pager i{width:5px;height:5px;border-radius:50%;background:var(--ink)}
.arrows{position:absolute;right:76px;top:535px;display:flex;gap:14px}
.arrows span{width:40px;height:40px;border:1.5px solid #C9B89E;border-radius:50%;display:flex;align-items:center;justify-content:center}

/* cta */
.cta{position:absolute;top:3137px;left:0;width:1200px;height:266px;background:var(--coral);color:var(--white);text-align:center}
.cta h2{margin-top:66px;font-size:38px;font-weight:500}
.cta p{width:530px;margin:20px auto 0;font-size:13px;line-height:23px}

/* lead form */
.lead-form{position:absolute;top:3403px;left:0;width:1200px;height:511px;background:var(--blush)}
.form-art{position:absolute;left:51px;top:143px;width:531px;height:368px;border-radius:260px 260px 0 0;background:linear-gradient(180deg,#FBD9D2,#F2A497 70%,#F0644E 100%)}
.step{position:absolute;left:693px;top:144px;font-size:11px;color:#B3A9A2}
.lead-form h3{position:absolute;left:693px;top:224px;font-size:17px;font-weight:500}
.choice{position:absolute;left:691px;width:341px;height:46px;border:1.5px solid var(--coral);border-radius:8px;color:var(--coral);display:flex;align-items:center;justify-content:center;font-size:14px;background:var(--white)}
.next{position:absolute;left:930px;top:428px;height:38px;width:100px;gap:8px}

/* blog */
.blog{position:absolute;top:3914px;left:0;width:1200px;height:899px;text-align:center}
.blog h2{margin-top:100px;font-size:38px;font-weight:500}
.blog .lead{margin-top:22px;font-size:13px}
.posts{position:absolute;left:53px;top:252px;display:flex;gap:41px;text-align:left}
.post{width:527px}
.post .thumb{height:243px;border-radius:12px}
.tag{margin-top:32px;font-size:10px;color:var(--coral);font-weight:500}
.post h3{margin-top:8px;font-size:19px;font-weight:500;line-height:28px}
.post p{margin-top:10px;font-size:12px;line-height:20px;color:var(--muted)}
.byline{display:flex;gap:14px;align-items:center;margin-top:16px;font-size:10px;line-height:16px}
.byline .avatar{width:38px;height:38px}
.view-all{position:absolute;left:555px;top:768px;width:90px;height:40px;border:1.5px solid var(--coral-soft);border-radius:30px;color:var(--coral);display:flex;align-items:center;justify-content:center;font-size:12px}

/* footer */
.site-footer{position:absolute;top:4813px;left:0;width:1200px;height:455px;background:var(--footer);color:var(--white)}
.site-footer .brand{position:absolute;left:53px;top:68px;color:var(--white);font-size:18px}
.quick{position:absolute;left:355px;top:68px;font-size:11px;list-style:none}
.quick li{margin-bottom:18px}
.quick li:first-child{font-weight:500;margin-bottom:22px}
.subscribe{position:absolute;left:730px;top:68px;width:418px;font-size:11px}
.subscribe h4{font-weight:500;font-size:11px;margin-bottom:22px}
.sub-row{display:flex;gap:10px;margin-top:18px}
.sub-row span{flex:1;height:40px;border-radius:30px;background:var(--white);color:#9a938e;display:flex;align-items:center;padding:0 12px;font-size:10px}
.sub-row b{width:100px;height:40px;border:1.5px solid var(--white);border-radius:30px;display:flex;align-items:center;justify-content:center;font-weight:500}
.fine{margin-top:14px;font-size:8.5px;line-height:14px;color:#E5DCD3}
.fine u{color:var(--white)}
.legal{position:absolute;left:53px;right:53px;top:334px;border-top:1px solid #5a4a3a;padding-top:28px;display:flex;justify-content:space-between;font-size:10px}
.legal nav{display:flex;gap:22px}
.legal nav a{text-decoration:underline}
.legal .left{display:flex;gap:22px}
.social{display:flex;gap:12px}
.social i{width:16px;height:16px;border-radius:50%;background:var(--white)}
</style>
</head>
<body>

<header class="site-nav">
  <a class="brand" href="#">Your Ridgeview Homefinder</a>
  <ul>
    <li>About Us</li><li>How it Works</li><li>Blog</li>
    <li><a class="btn" href="#">Contact Us</a></li>
  </ul>
</header>

<section class="hero">
  <div class="hero-photo" role="img" aria-label="Log cabin home beside a lake surrounded by tall pine trees"></div>
  <h1>Your Ridgeview Homefinder:<br>Your Perfect Match in Real Estate</h1>
  <form class="search">
    <div class="search-tabs"><span>Buy</span><span class="on">Sell</span></div>
    <div class="search-bar">
      <div class="field"><b>Property Type</b><span style="font-size:10px;color:#6d6762">Select Property Type &#8964;</span></div>
      <div class="field"><b>Location</b><i>eg. Littleton, Belmar</i></div>
      <div class="field"><b>Price Range</b><i>Min. Price-Max. Price</i></div>
      <span class="btn">Search</span>
    </div>
  </form>
</section>

<section class="intro">
  <h2>Making Real Estate Connections<br>Easy and Effective!</h2>
  <p>At Your Ridgeview Homefinder, we understand that finding the right realtor can make all the difference in your real estate journey. Whether you're looking to buy your dream home or sell your property for the best price, our mission is to connect you with the perfect realtor who understands your unique needs and goals.</p>
  <div class="rule"></div>
  <div class="featured">FEATURED IN</div>
  <div class="press"><span>Ledgerline</span><span>Market Courier</span><span>Capstone Weekly</span></div>
  <div class="intro-art" role="img" aria-label="Illustration of coral and pink townhouses and an apartment block with trees"></div>
</section>

<section class="why">
  <div class="why-photo" role="img" aria-label="Realtor handing house keys to a smiling couple"></div>
  <div class="agent-card">
    <div class="avatar" role="img" aria-label="Agent portrait"></div>
    <div><b style="font-weight:500">Arnold B.</b><br>Summit Key Realty<div class="stars">★★★★★</div></div>
  </div>
  <div class="sold-card">
    <div class="dot" role="img" aria-label="Small house illustration"></div>
    <div><strong>315</strong>Homes sold in Denver</div>
  </div>
  <h2>Why Choose Us?</h2>
  <ul class="features">
    <li><span class="icon"><svg width="20" height="20" viewBox="0 0 20 20" fill="none" stroke="#F0644E" stroke-width="1.5"><circle cx="6" cy="5" r="2.5"/><circle cx="14" cy="5" r="2.5"/><path d="M3 18v-6a3 3 0 016 0v6M11 18v-6a3 3 0 016 0v6"/></svg></span>
      <div><h3>Tailored Matches</h3><p>We take the time to understand your specific requirements and preferences, ensuring that we match you with a realtor who specializes in your desired neighborhood, property type, and budget.</p></div></li>
    <li><span class="icon"><svg width="20" height="20" viewBox="0 0 20 20" fill="none" stroke="#F0644E" stroke-width="1.5"><path d="M6 2h8v6a4 4 0 01-8 0z"/><path d="M10 12v4M6 18h8M6 4H3a3 3 0 003 4M14 4h3a3 3 0 01-3 4"/></svg></span>
      <div><h3>Experienced Professionals</h3><p>Our network of realtors consists of top-rated professionals with extensive knowledge of the Denver real estate market. They are dedicated to providing exceptional service and achieving the best outcomes for their clients.</p></div></li>
    <li><span class="icon"><svg width="20" height="20" viewBox="0 0 20 20" fill="none" stroke="#F0644E" stroke-width="1.5"><circle cx="5" cy="4" r="2"/><circle cx="15" cy="16" r="2"/><path d="M5 6v4a3 3 0 003 3h4a3 3 0 013 3"/></svg></span>
      <div><h3>Streamlined Process</h3><p>Say goodbye to the hassle of searching for a realtor on your own. Our streamlined process makes it easy and stress-free to find the perfect match, so you can focus on what matters most – your next move.</p></div></li>
  </ul>
</section>

<section class="stories">
  <h2>Success Stories</h2>
  <p class="lead">Listen to the experience of our happy clients.</p>
  <div class="quotes">
    <article class="quote"><p>"Working with Your Ridgeview Homefinder was a game-changer. They connected us with a fantastic realtor who helped us sell our home quickly and for a great price. The process was smooth and stress-free!"</p>
      <div class="who"><div class="avatar" role="img" aria-label="Client portrait"></div><div>Sarah and John M.<br><span>Satisfied Clients</span></div></div></article>
    <article class="quote"><p>"As first-time homebuyers, we were nervous about the process, but Your Ridgeview Homefinder made it so easy. They matched us with an experienced realtor who guided us every step of the way."</p>
      <div class="who"><div class="avatar" role="img" aria-label="Client portrait"></div><div>Emily R.<br><span>Happy Homeowner</span></div></div></article>
    <article class="quote"><p>"I had a tight deadline to sell my house and move for a new job. Your Ridgeview Homefinder matched me with a realtor who was incredibly efficient and effective. My house sold in record time, and I couldn't be happier with the service."</p>
      <div class="who"><div class="avatar" role="img" aria-label="Client portrait"></div><div>Michael T.<br><span>Relocated Professional</span></div></div></article>
    <article class="quote"></article>
  </div>
  <div class="pager"><i></i><i></i><i></i><i></i><i></i></div>
  <div class="arrows">
    <span><svg width="14" height="14" viewBox="0 0 14 14" fill="none" stroke="#1E1A17" stroke-width="1.4"><path d="M12 7H2M6 3L2 7l4 4"/></svg></span>
    <span><svg width="14" height="14" viewBox="0 0 14 14" fill="none" stroke="#1E1A17" stroke-width="1.4"><path d="M2 7h10M8 3l4 4-4 4"/></svg></span>
  </div>
</section>

<section class="cta">
  <h2>Get Started Today!</h2>
  <p>Ready to find the perfect realtor for your real estate journey? Fill out the form today and let Your Ridgeview Homefinder connect you with the best professional to meet your needs. Your dream home or ideal sale is just a click away!</p>
</section>

<section class="lead-form">
  <div class="form-art" role="img" aria-label="Illustration of pink and white houses with stylised trees"></div>
  <span class="step">Step 1 of 13</span>
  <h3>Are you looking to buy or sell a home?</h3>
  <span class="choice" style="top:280px">Buy a home</span>
  <span class="choice" style="top:350px">Sell a home</span>
  <span class="btn next">Next <svg width="12" height="12" viewBox="0 0 14 14" fill="none" stroke="#fff" stroke-width="1.6"><path d="M2 7h10M8 3l4 4-4 4"/></svg></span>
</section>

<section class="blog">
  <h2>Tips and Advice on our Blog</h2>
  <p class="lead">Lorem ipsum dolor sit amet, consectetur adipiscing elit.</p>
  <div class="posts">
    <article class="post">
      <div class="thumb" role="img" aria-label="Row of colourful beach town houses under a blue sky" style="background:linear-gradient(180deg,#9cc3e0 0%,#c9b58a 55%,#6f7f5c 100%)"></div>
      <div class="tag">Trends</div>
      <h3>America's Top 10 Most Affordable Beach Towns<br>for Retirees</h3>
      <p>Over the next four years, more than 16 million Americans will turn 65;<br>and many will explore the feasibility of moving to the beach.</p>
      <div class="byline"><div class="avatar" role="img" aria-label="Author portrait"></div><div>Wade Warren<br>11 Jun 2024 &nbsp;•&nbsp; 5 min read</div></div>
    </article>
    <article class="post">
      <div class="thumb" role="img" aria-label="Small wooden house models standing on a printed chart" style="background:linear-gradient(180deg,#eef0f3 0%,#dfe3e8 60%,#c7d6c4 100%)"></div>
      <div class="tag">News</div>
      <h3>Mortgage Rates Dip to 6.89% as Home Prices<br>Finally Take a Plunge</h3>
      <p>The real estate market was sluggish due to Independence Day.<br>Fewer sellers listed new homes, yet home prices finally plunged.</p>
      <div class="byline"><div class="avatar" role="img" aria-label="Author portrait"></div><div>Robert Fox<br>29 Jul 2024 &nbsp;•&nbsp; 5 min read</div></div>
    </article>
  </div>
  <a class="view-all" href="#">View all</a>
</section>

<footer class="site-footer">
  <span class="brand">Your Ridgeview Homefinder</span>
  <ul class="quick"><li>Quick Links</li><li>About Us</li><li>How it Works</li><li>Blog</li><li>Contact Us</li></ul>
  <div class="subscribe">
    <h4>Subscribe</h4>
    <p>Join our newsletter to stay up to date on features and releases.</p>
    <div class="sub-row"><span>Enter your email</span><b>Subscribe</b></div>
    <p class="fine">By subscribing you agree to with our <u>Privacy Policy</u> and provide consent to receive updates<br>from our company.</p>
  </div>
  <div class="legal">
    <div class="left"><span>© 2024 Your Ridgeview Homefinder. All rights reserved.</span>
      <nav><a href="#">Privacy Policy</a><a href="#">Terms of Service</a><a href="#">Cookies Settings</a></nav></div>
    <div class="social" aria-label="Social links"><i></i><i></i><i></i><i></i><i></i></div>
  </div>
</footer>

</body>
</html>
```